Law firm Seeks Modern and Engaging Site Redesign

Law firm seeks a new web site. Should be modern, but retaining existing logo. Needs to include contact section, professional bio, services offered, and contact information.

The site should be modern, responsive, and able to be SEO optimized.

The finished product should be coded in a Wordpress site, which I will provide. I can work with other platforms, including Wix, but WP is preferred.

Note the current site is https://www.tallowfieldlaw.example/#/home

Target Market(s)

Family Law Practice

Industry/Entity Type

Legal

Coding

Coded - Design and coding required

Number of Pages Required

4 page

Font styles to use
Sans Serif

Requirements
Must have
• Service description
Bio pages for partners
Contact Form
Awards/Publication page

```html
<!DOCTYPE html>
<html lang="en">
<head>
<meta charset="utf-8">
<title>Tallowfield &amp; Marsh — Attorneys at Law</title>
<link href="https://fonts.googleapis.com/css2?family=Roboto:wght@300;400;500;700&display=swap" rel="stylesheet">
<style>
:root{
  --blue:#2f6fc0;
  --blue-dark:#2a64ad;
  --navy:#1c3d66;
  --ink:#2b2b2b;
  --muted:#555;
  --footer:#232323;
  --line:#bfc5cc;
  --white:#fff;
}
*{box-sizing:border-box;margin:0;padding:0}
html,body{width:1200px;height:5309px;overflow:hidden}
body{font-family:'Roboto',Arial,sans-serif;color:var(--ink);background:var(--white);position:relative}
.abs{position:absolute}
.btn{position:absolute;display:flex;align-items:center;justify-content:center;background:var(--blue);color:var(--white);font-weight:500;font-size:17px;border-radius:2px}
.btn-outline{position:absolute;display:flex;align-items:center;justify-content:center;border:3px solid var(--blue);color:var(--blue);font-size:16px;background:var(--white)}

/* header */
.site-header{position:absolute;left:0;top:0;width:1200px;height:90px;background:var(--white);box-shadow:0 1px 4px rgba(0,0,0,.12);z-index:2}
.brand{position:absolute;left:72px;top:26px;font-size:25px;font-weight:400;color:#6a6f76;letter-spacing:.3px}
.header-contact{position:absolute;left:346px;top:16px;font-size:16px;color:var(--ink);line-height:32px}
.header-contact div{display:flex;align-items:center;gap:9px}
.main-nav{position:absolute;right:74px;top:34px;display:flex;gap:24px;font-size:14px;font-weight:500;color:#333}
.main-nav .active{color:var(--blue)}

/* hero */
.hero{position:absolute;left:0;top:90px;width:1200px;height:564px;background:linear-gradient(100deg,#5e5a55 0%,#8e8a84 30%,#6d6a66 55%,#9c9892 78%,#5c5955 100%)}
.hero-shade{position:absolute;inset:0;background:linear-gradient(180deg,rgba(0,0,0,.25),rgba(0,0,0,.1) 60%,rgba(255,255,255,.25))}
.hero-title{position:absolute;left:0;width:1200px;top:196px;text-align:center;color:var(--white);font-size:46px;font-weight:300}
.hero-sub{position:absolute;left:0;width:1200px;top:270px;text-align:center;color:var(--white);font-size:25px;font-weight:700}

/* about */
.statue{position:absolute;left:20px;top:760px;width:500px;height:398px;background:radial-gradient(ellipse at 60% 55%,#c79a3e,#9b6e22 55%,rgba(255,255,255,0) 75%)}
.about-block{position:absolute;left:165px;top:952px;width:290px;height:207px;background:#cfcfcf}
.about-corner{position:absolute;left:454px;top:1089px;width:50px;height:70px;border:5px solid var(--blue);border-left:none;border-bottom:none}
.years{position:absolute;left:150px;top:1159px;width:376px;height:62px;background:var(--blue);color:var(--white);font-size:26px;font-weight:500;display:flex;align-items:center;justify-content:center}
.about-title{position:absolute;left:577px;top:757px;font-size:35px;font-weight:700;color:var(--blue)}
.about-text{position:absolute;left:577px;top:822px;width:548px;font-size:21.5px;line-height:27px;color:var(--ink)}
.about-text p+p{margin-top:27px}

/* partners band */
.partners-band{position:absolute;left:0;top:1300px;width:1200px;height:474px;background:var(--navy)}
.partners-photo{position:absolute;left:177px;top:0;width:848px;height:474px;background:linear-gradient(90deg,#cfd3d8,#eef0f2 50%,#c9ccd0)}
.story{position:absolute;left:80px;top:1816px;width:1040px;text-align:center;font-size:21px;line-height:27px;color:#333}
.story p+p{margin-top:27px}

/* team */
.member{position:absolute;width:380px;text-align:center}
.avatar{width:166px;height:166px;border-radius:50%;margin:0 auto;background:linear-gradient(160deg,#b9bec4,#5b6470)}
.member-name{font-size:26px;font-weight:700;margin-top:22px;color:var(--ink)}

/* services */
.section-title{position:absolute;left:0;width:1200px;text-align:center;font-size:37px;font-weight:700;color:var(--blue)}
.services-band{position:absolute;left:0;top:2953px;width:1200px;height:326px;background:linear-gradient(180deg,#3a3e44 0%,#bfbfbd 35%,#8b5c34 60%,#6f4526 100%)}
.service{position:absolute;width:320px;text-align:center}
.service-img{width:306px;height:233px;margin:0 auto}
.service-title{margin-top:20px;font-size:27px;font-weight:500;color:var(--blue);text-transform:uppercase}
.service-text{margin:12px auto 0;width:318px;font-size:18px;line-height:21.6px;color:#333}

/* contact */
.contact-band{position:absolute;left:0;top:3712px;width:1200px;height:660px;background:var(--navy)}
.contact-title{position:absolute;left:0;width:1200px;top:40px;text-align:center;color:var(--white);font-size:35px;font-weight:700}
.map{position:absolute;left:315px;top:105px;width:570px;height:431px;background:linear-gradient(135deg,#e8eaed,#f4f4f2 45%,#cfe3f0 70%,#e6e8ea)}
.contact-info{position:absolute;top:592px;display:flex;align-items:center;gap:14px;color:var(--white);font-size:18px;line-height:22px}

/* enquiry */
.field{position:absolute;left:326px;width:546px;height:65px;border:2px solid var(--line);display:flex;align-items:center;background:var(--white)}
.field-icon{width:54px;height:100%;border-right:2px solid var(--line);display:flex;align-items:center;justify-content:center}
.field-label{padding-left:16px;font-size:17px;font-weight:500;color:#222}

/* footer */
.site-footer{position:absolute;left:0;top:4940px;width:1200px;height:369px;background:var(--footer);color:#e6e6e6}
.footer-brand{position:absolute;left:72px;top:58px;font-size:30px;font-weight:400;color:#e9e9e9}
.footer-about{position:absolute;left:72px;top:133px;width:320px;font-size:17px;line-height:30px}
.footer-col{position:absolute;top:58px}
.footer-col h3{font-size:25px;font-weight:700;color:var(--white);margin-bottom:14px}
.footer-col li{list-style:none;font-size:17px;line-height:30px}
.copyright{position:absolute;left:0;width:1200px;top:336px;text-align:center;font-size:13px;color:#ddd}
</style>
</head>
<body>

<header class="site-header">
  <div class="brand">Tallowfield &amp; Marsh</div>
  <div class="header-contact">
    <div>
      <svg width="22" height="22" viewBox="0 0 24 24"><circle cx="12" cy="12" r="10.5" fill="none" stroke="#333" stroke-width="1.8"/><path d="M8.5 7c.6-.6 1.3-.4 1.6.2l.9 1.7c.3.5.1 1-.3 1.3l-.6.5c.5 1.2 1.5 2.3 2.8 2.9l.5-.6c.4-.4 1-.5 1.4-.2l1.6 1c.5.4.6 1.1.1 1.6-1 1-2.5 1.2-4 .4-2.2-1.2-3.8-2.9-4.7-5-.6-1.4-.3-2.9.7-3.8z" fill="#333"/></svg>
      <span>(555) 014-2141</span>
    </div>
    <div>
      <svg width="22" height="22" viewBox="0 0 24 24"><circle cx="12" cy="12" r="10.5" fill="none" stroke="#333" stroke-width="1.8"/><rect x="7" y="8.5" width="10" height="7" fill="none" stroke="#333" stroke-width="1.5"/><path d="M7 8.5l5 4 5-4" fill="none" stroke="#333" stroke-width="1.5"/></svg>
      <span>contact@tallowfieldlaw.example</span>
    </div>
  </div>
  <nav class="main-nav">
    <span class="active">Home</span><span>Family Law</span><span>Criminal Law</span><span>About</span><span>Partners</span><span>Contact</span>
  </nav>
</header>

<section class="hero" role="img" aria-label="Courthouse columns and stone steps">
  <div class="hero-shade"></div>
  <h1 class="hero-title">Tallowfield &amp; Marsh</h1>
  <p class="hero-sub">Attorney's at the law.</p>
  <div class="btn" style="left:510px;top:337px;width:180px;height:37px;font-weight:400;font-size:18px">Contact Us</div>
</section>

<section class="about">
  <div class="about-block"></div>
  <div class="about-corner"></div>
  <div class="statue" role="img" aria-label="Gilded statue of Lady Justice holding scales and sword"></div>
  <div class="years">30+ Years of experience</div>
  <h2 class="about-title">About Tallowfield &amp; Marsh</h2>
  <div class="about-text">
    <p>The law firm of Tallowfield Marsh, LLC is based in Alder County, conveniently located in Brookhaven, New Jersey in 40 Collegiate Plaza. We serve the needs of clients throughout Alder County, as well as, clients from several other counties, including, but not limited to, Pinecrest, Morrow, Easton and Harborview. Between our partners, we have over 30+ years of experience assisting clients with all of their family law and criminal law needs.</p>
    <p>Often times the areas of family law and criminal law cross paths, which can be both emotionally and financially complex. We understand that our client's case is unique and pride ourselves on being responsive to all of our clients needs.</p>
  </div>
</section>

<section class="partners-band">
  <div class="partners-photo" role="img" aria-label="The two founding partners standing in the firm's office lobby"></div>
</section>

<section class="story">
  <p>Mr. Tallowfield began his career as the law clerk to the Honorable Harold T. Quinlan, J.S.C., retired, the then Presiding Judge of the Criminal Part and thereafter as an Assistant Prosecutor with the Alder County Prosecutors Office. Mr. Marsh began his career as the law clerk to the Honorable George D. Whitcombe, J.S.C., retired, who oversaw the Court's Juvenile Delinquency docket, DCWS (now DCF&amp;S) docket and all other Family Part matters. As a result of their experience in the court system, Mr. Tallowfield and Mr. Marsh bring a unique perspective to their practice.</p>
  <p>Both Mr. Tallowfield and Mr. Marsh practiced privately for well over a decade as partners in two of Alder County's most established Family Law firms before joining together to use their knowledge and experience to assist their clients with all of their legal needs.</p>
  <p>Whether your needs are family or criminal law related, contact Tallowfield Marsh, LLC to schedule a consultation.</p>
</section>

<section class="team">
  <div class="member" style="left:10px;top:2258px"><div class="avatar" role="img" aria-label="Portrait of Daniel R. Tallowfield"></div><div class="member-name">Daniel R. Tallowfield, Esq.</div></div>
  <div class="btn" style="left:130px;top:2487px;width:140px;height:53px">Know More</div>
  <div class="btn-outline" style="left:89px;top:2567px;width:221px;height:52px">Rated by Peer Counsel</div>

  <div class="member" style="left:420px;top:2258px"><div class="avatar" role="img" aria-label="Portrait of Owen P. Marsh"></div><div class="member-name">Owen P. Marsh, Esq.</div></div>
  <div class="btn" style="left:540px;top:2487px;width:140px;height:53px">Know More</div>
  <div class="btn-outline" style="left:499px;top:2567px;width:221px;height:52px">Rated by Peer Counsel</div>

  <div class="member" style="left:822px;top:2258px"><div class="avatar" role="img" aria-label="Portrait of Laura M. Penrose"></div><div class="member-name">Laura M. Penrose, Esq.</div></div>
  <div class="btn" style="left:942px;top:2487px;width:140px;height:53px">Know More</div>
  <div class="btn-outline" style="left:900px;top:2567px;width:221px;height:52px">Rated by Peer Counsel</div>

  <div class="abs" style="left:0;width:1200px;top:2700px;text-align:center;font-size:26px;font-weight:700">Sofia N. Ravell</div>
  <div class="btn" style="left:530px;top:2759px;width:140px;height:52px">Know More</div>
</section>

<section class="services">
  <h2 class="section-title" style="top:2891px">Law Services Offered</h2>
  <div class="services-band" role="img" aria-label="Empty courtroom with wooden benches"></div>
  <div class="service" style="left:81px;top:3149px">
    <div class="service-img" role="img" aria-label="Judge's gavel resting on law books" style="background:linear-gradient(135deg,#e9e7e3,#7a6c5c 60%,#4a2f1d)"></div>
    <h3 class="service-title">Criminal Law</h3>
    <p class="service-text">Lorem ipsum dolor sit amet, consectetur adipiscing elit, sed do eiusmod tempor incididunt ut labore et dolore magna aliqua. Dolor sit amet consectetur adipiscing. In dictum non consectetur a erat nam at lectus urna. Hendrerit gravida rutrum quisque non tellus orci ac auctor. Purus in mollis nunc sed id.</p>
  </div>
  <div class="service" style="left:438px;top:3149px">
    <div class="service-img" role="img" aria-label="Lawyer in a suit at a desk explaining documents" style="background:linear-gradient(135deg,#dfe4ea,#2b3a55 55%,#e8eaec)"></div>
    <h3 class="service-title">Corporate Law</h3>
    <p class="service-text">Lorem ipsum dolor sit amet, consectetur adipiscing elit, sed do eiusmod tempor incididunt ut labore et dolore magna aliqua. Dolor sit amet consectetur adipiscing. In dictum non consectetur a erat nam at lectus urna. Hendrerit gravida rutrum quisque non tellus orci ac auctor. Purus in mollis nunc sed id.</p>
  </div>
  <div class="service" style="left:813px;top:3149px">
    <div class="service-img" role="img" aria-label="Hand signing a will with a pen" style="background:linear-gradient(135deg,#eef0f3,#c9a98e 55%,#f2f2f2)"></div>
    <h3 class="service-title">Wills &amp; Property</h3>
    <p class="service-text">Lorem ipsum dolor sit amet, consectetur adipiscing elit, sed do eiusmod tempor incididunt ut labore et dolore magna aliqua. Dolor sit amet consectetur adipiscing. In dictum non consectetur a erat nam at lectus urna. Hendrerit gravida rutrum quisque non tellus orci ac auctor. Purus in mollis nunc sed id.</p>
  </div>
</section>

<section class="contact-band">
  <h2 class="contact-title">Contact Us</h2>
  <div class="map" role="img" aria-label="Street map showing the office location in Brookhaven"></div>
  <div class="contact-info" style="left:72px">
    <svg width="28" height="28" viewBox="0 0 24 24"><circle cx="12" cy="12" r="10.5" fill="none" stroke="#fff" stroke-width="1.5"/><path d="M12 6.5a3.5 3.5 0 0 0-3.5 3.5c0 2.6 3.5 7 3.5 7s3.5-4.4 3.5-7A3.5 3.5 0 0 0 12 6.5z" fill="none" stroke="#fff" stroke-width="1.4"/><circle cx="12" cy="10" r="1.2" fill="#fff"/></svg>
    <span>40 Collegiate Plaza Drive Suite 312<br>Brookhaven, NJ 07000</span>
  </div>
  <div class="contact-info" style="left:526px;top:600px">
    <svg width="28" height="28" viewBox="0 0 24 24"><circle cx="12" cy="12" r="10.5" fill="none" stroke="#fff" stroke-width="1.5"/><path d="M8.5 7c.6-.6 1.3-.4 1.6.2l.9 1.7c.3.5.1 1-.3 1.3l-.6.5c.5 1.2 1.5 2.3 2.8 2.9l.5-.6c.4-.4 1-.5 1.4-.2l1.6 1c.5.4.6 1.1.1 1.6-1 1-2.5 1.2-4 .4-2.2-1.2-3.8-2.9-4.7-5-.6-1.4-.3-2.9.7-3.8z" fill="#fff"/></svg>
    <span>(555) 014-2141</span>
  </div>
  <div class="contact-info" style="left:824px;top:600px">
    <svg width="28" height="28" viewBox="0 0 24 24"><circle cx="12" cy="12" r="10.5" fill="none" stroke="#fff" stroke-width="1.5"/><rect x="7" y="8.5" width="10" height="7" fill="none" stroke="#fff" stroke-width="1.4"/><path d="M7 8.5l5 4 5-4" fill="none" stroke="#fff" stroke-width="1.4"/></svg>
    <span>contact@tallowfieldlaw.example</span>
  </div>
</section>

<section class="enquiry">
  <h2 class="section-title" style="top:4456px">Submit an Enquiry</h2>
  <div class="field" style="top:4532px">
    <div class="field-icon"><svg width="26" height="26" viewBox="0 0 24 24" fill="none" stroke="#333" stroke-width="1.5"><circle cx="12" cy="7" r="3.5"/><path d="M5 21v-3a5 5 0 0 1 5-5h4a5 5 0 0 1 5 5v3z"/></svg></div>
    <span class="field-label">Your Name*</span>
  </div>
  <div class="field" style="top:4625px">
    <div class="field-icon"><svg width="26" height="26" viewBox="0 0 24 24"><path d="M6 4c.8-.8 1.8-.6 2.2.3l1.3 2.4c.4.7.2 1.4-.4 1.8l-.9.7c.8 1.8 2.2 3.2 4 4l.7-.9c.5-.6 1.2-.7 1.8-.3l2.3 1.4c.8.5.9 1.5.2 2.2-1.5 1.5-3.6 1.7-5.6.6C8.6 14.6 6.4 12.3 5 9.3 4.2 7.4 4.6 5.3 6 4z" fill="none" stroke="#333" stroke-width="1.4"/></svg></div>
    <span class="field-label">Your Contact Number*</span>
  </div>
  <div class="field" style="top:4720px">
    <div class="field-icon"><svg width="26" height="26" viewBox="0 0 24 24" fill="none" stroke="#333" stroke-width="1.5"><rect x="4" y="5" width="16" height="14" rx="1"/><circle cx="9.5" cy="10.5" r="2"/><path d="M6.5 16c.5-1.7 1.7-2.5 3-2.5s2.5.8 3 2.5M14 10h4M14 13h4"/></svg></div>
    <span class="field-label">Your E-mail Adress</span>
  </div>
  <div class="btn" style="left:485px;top:4813px;width:229px;height:54px;font-size:20px;font-weight:700">Submit</div>
</section>

<footer class="site-footer">
  <div class="footer-brand">Tallowfield &amp; Marsh</div>
  <p class="footer-about">Lorem ipsum dolor sit amet, consectetur adipiscing elit, sed do eiusmod tempor incididunt ut labore et dolore magna aliqua. Quis ipsum suspendisse ultrices gravida. Risus</p>
  <div class="footer-col" style="left:470px">
    <h3>Contact Us</h3>
    <ul><li>Tallowfield &amp; Marsh LLC</li><li>40 Collegiate Plaza Drive Suite 312</li><li>Brookhaven, NJ 07000</li><li>(555) 014-2141 Phone</li><li>(555) 014-1257 Fax</li><li>Tallowfield &amp; Marsh, LLC</li></ul>
  </div>
  <div class="footer-col" style="left:815px">
    <h3>Quick links</h3>
    <ul><li>Services</li><li>Partners</li><li>About Us</li><li>Family law</li><li>Criminal law</li></ul>
  </div>
  <div class="footer-col" style="left:1027px">
    <h3>Sitemap</h3>
    <ul><li>Home</li><li>About Us</li><li>Awards</li><li>Publication</li><li>Contact Us</li></ul>
  </div>
  <p class="copyright">Copyright © 2020 Tallowfield &amp; Marsh LLC pvt ltd.</p>
</footer>

</body>
</html>
```